Criação de Apres. Comercial (com dobra) para Limpeza & Serviço para o lar
A empresa queria:
" No mercado desde 2001, a Vento Sereno tem como Missão oferecer aos clientes a mais alta qualidade na prestação de serviço3s e manter a confiabilidade conquistada. Nosso posicionamento é o de parceria, no sentido de ajudar nossos clientes a viabilizar seus objetivos e projetos, mantendo-os focados em sua atividade principal. Serviços personalizados, com Mão-de-obra Terceirizada e bem treinada, acompanhados por constante Supervisão, de acordo com as necessidades e características de cada cliente, detectando pontos de melhoria e execução das tarefas de forma clara e precisa. Auxiliares de Serviços Gerais, Controladores de Acesso, Zeladores, Ascensoristas, Recepcionistas, Jardineiros, Copeiras, Garagistas, Limpadores de Vidro, Auxiliares de Manutenção, Telefonistas, Mensageiros, Auxiliares Administrativos. "

```html
<!DOCTYPE html>
<html lang="pt-BR">
<head>
<meta charset="utf-8">
<title>Vento Sereno – Apresentação Comercial</title>
<link rel="stylesheet" href="https://fonts.googleapis.com/css2?family=Arimo:wght@400;700&family=Montserrat:wght@700&display=swap">
<style>
  :root{
    --bg:#e9ecee;
    --paper:#ffffff;
    --teal-dark:#0f4c57;
    --teal:#1b8794;
    --aqua:#5ec5cf;
    --aqua-pale:#cdecef;
    --ink:#1d2a2f;
    --photo-a:#8fa07a;
    --photo-b:#c9cdc6;
  }
  *{box-sizing:border-box;margin:0;padding:0}
  html,body{width:1200px;height:1200px;overflow:hidden;background:var(--bg)}
  body{font-family:"Arimo",Arial,sans-serif;color:var(--ink)}
  .folder{position:absolute;left:180px;top:220px;width:840px;height:760px;display:flex;box-shadow:0 10px 30px rgba(0,0,0,.18)}
  .panel{position:relative;width:420px;height:760px;background:var(--paper);overflow:hidden}

  /* back panel */
  .photos{position:absolute;left:22px;top:32px;width:376px;height:176px;display:flex;gap:10px}
  .photo-stack{flex:1;display:flex;flex-direction:column;gap:6px}
  .photo{flex:1}
  .photo--gardener-top{background:linear-gradient(135deg,#5d7444,var(--photo-a))}
  .photo--gardener-bottom{background:linear-gradient(135deg,#7c8a6a,#d9dcd2)}
  .photo--cleaner{flex:1;background:linear-gradient(160deg,#f1f1ee,var(--photo-b) 60%,#d9c24a)}
  .brand-band{position:absolute;left:0;top:232px;width:420px;height:122px;background:var(--teal-dark);display:flex;flex-direction:column;align-items:center;justify-content:center;gap:10px}
  .brand-band .dot{width:34px;height:34px;border-radius:50%;background:var(--aqua)}
  .brand-name{font-family:"Montserrat",Arial,sans-serif;font-weight:700;color:#fff;font-size:22px}
  .accent-line{position:absolute;left:0;top:360px;width:420px;height:8px;background:var(--aqua)}
  .contact-title{position:absolute;top:418px;width:420px;text-align:center;font-weight:700;font-size:13px;letter-spacing:.3px}
  .contact{position:absolute;left:18px;top:470px;font-size:11px;line-height:16px}
  .contact-head{display:flex;align-items:center;gap:6px;font-weight:700;font-size:12px;margin-bottom:26px}
  .contact-head svg{width:14px;height:14px}
  .contact b{font-weight:700}
  .contact a{color:var(--ink)}
  .base-band{position:absolute;left:0;bottom:26px;width:420px;height:12px;background:var(--teal)}

  /* cover */
  .cover-swoosh{position:absolute;inset:0}
  .cover-brand{position:absolute;left:70px;top:300px;width:330px;display:flex;flex-direction:column;align-items:center;gap:16px}
  .cover-brand .dot{width:74px;height:74px;border-radius:50%;background:var(--teal)}
  .cover-brand .brand-name{color:var(--teal-dark);font-size:34px}
  .tagline-band{position:absolute;left:90px;top:555px;width:330px;height:40px;background:linear-gradient(90deg,var(--aqua-pale),var(--aqua));display:flex;align-items:center;padding-left:22px;font-size:12.5px;font-weight:700;color:var(--teal-dark)}
</style>
</head>
<body>
<main class="folder">
  <section class="panel panel--back">
    <div class="photos">
      <div class="photo-stack">
        <div class="photo photo--gardener-top" role="img" aria-label="Foto de jardineiro podando plantas"></div>
        <div class="photo photo--gardener-bottom" role="img" aria-label="Foto de jardineiro com uniforme e luvas"></div>
      </div>
      <div class="photo photo--cleaner" role="img" aria-label="Foto de profissional de limpeza com carrinho de produtos"></div>
    </div>
    <div class="brand-band">
      <span class="dot"></span>
      <span class="brand-name">Vento Sereno</span>
    </div>
    <div class="accent-line"></div>
    <h2 class="contact-title">ENTRE EM CONTATO CONOSCO</h2>
    <div class="contact">
      <div class="contact-head">
        <svg viewBox="0 0 14 14"><circle cx="7" cy="7" r="7" fill="#1d2a2f"/><path d="M4 6h6M4 8.5h4" stroke="#fff" stroke-width="1.3"/></svg>
        Informações Cadastrais
      </div>
      <p><b>Telefone:</b> (11) 4820-3170</p>
      <p><b>Endereço:</b> Rua das Acácias, 48 - Jardim Aurora - São Paulo - SP - 04512-030</p>
      <p><b>Site:</b> <a>www.ventosereno.com.br</a></p>
      <p><b>Email:</b> contato@ventosereno.com.br</p>
    </div>
    <div class="base-band"></div>
  </section>

  <section class="panel panel--cover">
    <svg class="cover-swoosh" viewBox="0 0 420 760" preserveAspectRatio="none" aria-hidden="true">
      <path d="M0 0 H46 C30 260 60 520 170 760 H0 Z" fill="var(--teal-dark)"/>
      <path d="M46 0 C30 260 60 520 170 760 H200 C90 540 58 280 66 0 Z" fill="var(--aqua)"/>
      <path d="M300 0 H420 V400 C410 220 370 90 300 0 Z" fill="var(--teal)"/>
      <path d="M300 0 C370 90 410 220 420 400 V430 C400 240 360 100 280 0 Z" fill="var(--aqua)"/>
    </svg>
    <div class="cover-brand">
      <span class="dot"></span>
      <span class="brand-name">Vento Sereno</span>
    </div>
    <div class="tagline-band">SERVIÇOS CRIADOS DO SEU JEITO.</div>
  </section>
</main>
</body>
</html>
```